Chiropractic healthcare group business card

We are a Portland Oregon based chiropractic healthcare group. Looking for a new business card design. Something cutting edge, that shows off our new logo and tag line.Use either of the attached logos.Our tag line = "How far could you go pain free?"I'm open to about anything, impress me!!
Target Market(s)
Chiropractic patients - Auto injury, back pain, sports injuries, neck , shoulder, hip, knee, ankle pain.
Industry/Entity Type
Chiropractic
Contact Information for Business Card
Dr. Bram Holtvick, D.C.
Clinic name - Fernway Chiropractic
2 clinics
location #1
20418 NW Marwick Road
Suite B
North Plains, OR 97133
Location #2
13529 SE Calloway Street
Portland OR 97236
Main phone line 971.555.0143
website : www.FernwayClinics.example
Tag line "How far could you go pain free?"
Colors
Designer to choose colors to be used in the design.
Requirements
Must have
- Use the logo colors -- Want the orange color to be a TRUE orange.
- Both clinic address
- phone number
- website
- personal email - b.holtvick@ReliefBeginsHere.example
- tag line - "How far could you go pain free?"

```html
<!DOCTYPE html>
<html lang="en">
<head>
<meta charset="utf-8">
<title>Fernway Chiropractic – Business Card</title>
<link rel="stylesheet" href="https://fonts.googleapis.com/css2?family=Montserrat:wght@300;400;600&family=Roboto+Condensed:wght@400&family=Kaushan+Script&display=swap">
<style>
  :root {
    --true-orange: #f7771c;
    --orange-light: #fa8a35;
    --ink-gray: #5a5a5a;
    --text-gray: #4a4a4a;
    --band-gray: #6b6b6b;
    --paper: #f7f7f5;
    --stage: #d9d9d9;
    --white: #ffffff;
  }
  * { margin: 0; padding: 0; box-sizing: border-box; }
  html, body { width: 1200px; height: 900px; overflow: hidden; }
  body {
    background: var(--stage);
    font-family: "Montserrat", sans-serif;
    position: relative;
  }
  .card {
    position: absolute;
    left: 250px;
    width: 700px;
    height: 400px;
    overflow: hidden;
  }

  /* Front */
  .card-front {
    top: 35px;
    background: linear-gradient(135deg, var(--true-orange) 0%, var(--orange-light) 100%);
    color: var(--white);
    text-align: center;
  }
  .brand-name {
    position: absolute;
    top: 120px;
    left: 0; right: 0;
    font-weight: 600;
    color: var(--white);
  }
  .brand-name .brand-main {
    display: block;
    font-size: 46px;
    letter-spacing: 18px;
    padding-left: 18px;
  }
  .brand-name .brand-sub {
    display: block;
    font-size: 15px;
    letter-spacing: 5px;
    padding-left: 5px;
    margin-top: 8px;
  }
  .tagline {
    position: absolute;
    top: 232px;
    left: 0; right: 0;
    font-family: "Kaushan Script", cursive;
    font-size: 34px;
  }
  .website {
    position: absolute;
    top: 310px;
    left: 0; right: 0;
    font-size: 12px;
    font-weight: 600;
    letter-spacing: 3.5px;
  }

  /* Back */
  .card-back {
    top: 465px;
    background: var(--paper);
    color: var(--text-gray);
  }
  .identity {
    position: absolute;
    top: 128px;
    right: 400px;
    text-align: right;
  }
  .identity .person-name {
    font-family: "Roboto Condensed", sans-serif;
    font-size: 31px;
    color: var(--true-orange);
    white-space: nowrap;
  }
  .identity .clinic-name {
    font-size: 14px;
    font-weight: 600;
    letter-spacing: 2.5px;
    color: var(--ink-gray);
    margin-top: 2px;
    white-space: nowrap;
  }
  .divider {
    position: absolute;
    left: 326px;
    top: 105px;
    width: 2px;
    height: 110px;
    background: var(--true-orange);
  }
  .contact-list {
    position: absolute;
    left: 352px;
    top: 114px;
    list-style: none;
  }
  .contact-list li {
    display: flex;
    align-items: center;
    gap: 12px;
    font-size: 15px;
    color: var(--text-gray);
    height: 30px;
    white-space: nowrap;
  }
  .contact-list li.email { font-size: 13px; }
  .contact-list svg { width: 14px; height: 14px; flex: none; }
  .locations {
    position: absolute;
    left: 0; right: 0;
    top: 256px;
    text-align: center;
    font-size: 14px;
    line-height: 24px;
  }
  .locations .locations-title {
    font-weight: 600;
    font-size: 15px;
    color: var(--ink-gray);
  }
  .locations .label { color: var(--true-orange); font-weight: 600; }
  .footer-band {
    position: absolute;
    left: 0; bottom: 0;
    width: 700px;
    height: 30px;
  }
  .corner-mark {
    position: absolute;
    left: 14px;
    bottom: 8px;
    font-size: 11px;
    font-weight: 600;
    color: var(--true-orange);
  }
</style>
</head>
<body>

<section class="card card-front" aria-label="Card front">
  <div class="brand-name">
    <span class="brand-main">FERNWAY</span>
    <span class="brand-sub">CHIROPRACTIC</span>
  </div>
  <p class="tagline">How far could you go pain free?</p>
  <p class="website">www.FernwayClinics.example</p>
</section>

<section class="card card-back" aria-label="Card back">
  <div class="identity">
    <p class="person-name">Dr. Bram Holtvick, D.C.</p>
    <p class="clinic-name">Fernway Chiropractic</p>
  </div>
  <div class="divider"></div>
  <ul class="contact-list">
    <li>
      <svg viewBox="0 0 16 16" aria-hidden="true"><path fill="var(--true-orange)" d="M3.6 1.5l2.2 2.6-1.2 1.6c.9 2 2.5 3.6 4.6 4.6l1.6-1.2 2.6 2.2-1.2 2.1C7 13.3 2.7 9 1.5 4l2.1-2.5z"/></svg>
      971.555.0143
    </li>
    <li>
      <svg viewBox="0 0 16 16" aria-hidden="true"><rect x="1" y="5" width="14" height="10" rx="1" fill="var(--true-orange)"/><rect x="4" y="1" width="8" height="5" fill="var(--true-orange)"/><rect x="7" y="8" width="6" height="5" fill="var(--paper)"/></svg>
      971.555.0178
    </li>
    <li class="email">
      <svg viewBox="0 0 16 16" aria-hidden="true"><path fill="var(--true-orange)" d="M15 1L1 7l5 2 1 6 2.5-4L13 13z"/></svg>
      b.holtvick@ReliefBeginsHere.example
    </li>
  </ul>
  <div class="locations">
    <p class="locations-title">Fernway Chiropractic</p>
    <p><span class="label">Portland Office :</span> 13529 SE Calloway St., Portland, OR 97236</p>
    <p><span class="label">North Plains :</span> 20418 NW Marwick Rd, Suite B, North Plains, OR 97133</p>
  </div>
  <svg class="footer-band" viewBox="0 0 700 30" preserveAspectRatio="none" aria-hidden="true">
    <polygon points="92,22 560,22 553,30 84,30" fill="var(--true-orange)"/>
    <polygon points="566,22 700,22 700,30 558,30" fill="var(--band-gray)"/>
  </svg>
  <span class="corner-mark">Fernway</span>
</section>

</body>
</html>
```